Shopify Design for wedding invitations

We are a greeting card manufactory, special in wedding invitation
I need a shopify website for our wedding invitation brand. (Lovmira), atttach you can find our logo.
We are looking for someone to create a modern and clean looking e-commerce store for our wedding invitation through Shopify. We need some life, professionalism and style put into our site. We will have a variety serie of products : laser cut wedding invitation, popup wedding invitaiton, vintage wedding invitation, handmade wedding invitation, printing invitation, Custom wedding cards, wedding stationery (including favor box, table card, place card, escort card, number card), Thank you card. our online store requires easy navigation to categories divided by product type.

our market is , Eourpe and USA,
please choose a good color for it.
you can go to our website: www.bluestonecraft.com and check our product.
also you can go to Vendoro 4 new items.
https://www.vendoro-shop.com/dp/X47K8Q2M19?ref=abc_item_dp

Target Market(s)

Europe and USA

Industry/Entity Type

wedding

Number of Pages Required

1 page

Requirements
Must have
• Logo, 3 banners than can be changed each 3-5 seconds.
Nice to have
• nice icon and font, beautiful color,

```html
<!DOCTYPE html>
<html lang="en">
<head>
<meta charset="utf-8">
<title>Lovmira – Wedding Invitations</title>
<link rel="stylesheet" href="https://fonts.googleapis.com/css2?family=Poppins:wght@400;500;600;700&family=Great+Vibes&display=swap">
<style>
:root{
  --brown:#4a2410;
  --brown-dark:#3a1a09;
  --green:#6b9b3a;
  --green-soft:#8db35a;
  --red:#e10a14;
  --price:#c8102e;
  --cream:#f7f1e7;
  --text:#3b3b3b;
  --muted:#8a8a8a;
  --white:#ffffff;
  --line:#e3ddd3;
}
*{box-sizing:border-box;margin:0;padding:0}
html,body{width:1200px;height:3772px;overflow:hidden}
body{font-family:'Poppins',sans-serif;color:var(--text);background:var(--white);position:relative}
.topbar{height:40px;background:var(--brown);color:var(--white);font-size:13px;font-weight:600;letter-spacing:.5px;display:flex;align-items:center;justify-content:center}
.header{height:128px;display:flex;align-items:center;padding:0 108px;justify-content:space-between}
.brand{font-size:40px;font-weight:600;color:var(--brown);display:flex;align-items:center;gap:10px}
.brand .dot{width:14px;height:14px;border-radius:50%;background:var(--red)}
.nav{display:flex;align-items:center;gap:34px;font-size:14px;font-weight:500;color:var(--text)}
.nav .active{color:var(--red)}
.nav .icon-btn{width:40px;height:40px;border-radius:50%;border:2px solid var(--red);display:flex;align-items:center;justify-content:center;margin-left:-18px}
.nav .icon-btn.cart{border-color:var(--green)}
.hero{height:652px;position:relative;background:linear-gradient(100deg,#3e2414 0%,#6a4226 35%,#8a5a34 60%,#c59c6a 80%,#a87a4a 100%)}
.hero-copy{position:absolute;left:40px;top:340px;color:var(--white)}
.hero-copy h1{font-family:'Great Vibes',cursive;font-weight:400;font-size:72px;line-height:1}
.hero-copy p{font-size:28px;line-height:36px;margin-top:20px;width:440px}
.btn{display:inline-block;border-radius:24px;color:var(--white);font-size:14px;font-weight:600;padding:11px 26px}
.hero-copy .btn{background:var(--green);margin-top:30px}
.dots{position:absolute;left:50%;bottom:20px;transform:translateX(-50%);display:flex;gap:10px}
.dots span{width:12px;height:12px;border-radius:50%;background:rgba(255,255,255,.5)}
.dots span.on{background:var(--white)}
.section-title{text-align:center;font-size:38px;font-weight:500;color:var(--brown-dark)}
.section-title::after{content:"";display:block;width:70px;height:3px;background:var(--brown);margin:12px auto 0}
.categories{height:580px;padding-top:62px}
.grid{display:flex;gap:12px;padding:0 108px}
.cat-card{width:238px;border:1px solid var(--line)}
.cat-card .media{height:312px}
.cat-card .label{height:68px;text-align:center;font-size:14px;line-height:20px;color:var(--text);padding-top:14px;border-top:3px solid var(--brown)}
.products{padding-top:62px}
.featured{height:632px;background:var(--cream)}
.new{height:640px;background:var(--cream)}
.product{width:238px;text-align:center}
.product .media{height:280px;position:relative}
.heart{position:absolute;top:12px;right:12px;width:34px;height:34px;border-radius:50%;background:var(--green);display:flex;align-items:center;justify-content:center}
.add-cart{position:absolute;left:50%;top:50%;transform:translate(-50%,-50%);background:var(--green);color:var(--white);font-size:12px;font-weight:600;padding:8px 22px;border-radius:18px}
.stars{margin-top:16px;color:#c9c9c9;font-size:13px;letter-spacing:2px}
.product h3{font-size:20px;font-weight:500;color:var(--text);margin-top:4px}
.product .model{font-size:11px;color:var(--muted)}
.product .price{font-size:22px;font-weight:600;color:var(--price);margin-top:4px}
.about{height:468px;position:relative;display:flex}
.about-copy{width:600px;background:linear-gradient(90deg,var(--green) 0%,var(--green-soft) 75%,#c7d9ad 100%);padding:96px 0 0 108px;color:var(--white)}
.about-copy h2{font-size:40px;font-weight:500;color:var(--brown-dark)}
.about-copy p{font-size:13px;line-height:20px;width:430px;margin-top:16px}
.about-copy .btn{background:var(--brown);margin-top:28px}
.about-media{flex:1;background:linear-gradient(90deg,#c7d9ad 0%,#e9efe2 30%,#f4e6e6 70%,#eec9cf 100%)}
.promo{height:292px;background:var(--red);display:flex;align-items:center;padding:0 80px;gap:64px;color:var(--white)}
.promo .art{width:320px;height:232px;background:rgba(255,255,255,.14);border-radius:8px}
.promo p{font-size:24px;line-height:34px;width:620px}
.promo .shop{font-size:40px;font-weight:700;margin-top:18px}
.footer{height:340px;background:var(--brown);color:var(--white);display:flex;padding:76px 0 0 108px;gap:0}
.footer .brand{color:var(--white)}
.foot-brand{width:364px}
.foot-brand small{display:block;font-size:13px;margin-top:50px}
.foot-col h4{font-size:18px;font-weight:600;margin-bottom:20px}
.foot-col.address{width:316px}
.foot-col.links{width:172px}
.info{display:flex;gap:12px;margin-bottom:14px;font-size:11px;line-height:15px}
.info b{display:block;font-size:13px;font-weight:600}
.circle{flex:none;width:34px;height:34px;border-radius:50%;border:1.5px solid var(--white);display:flex;align-items:center;justify-content:center}
.links ul{list-style:none;font-size:13px;line-height:30px}
.links li::before{content:"›";margin-right:10px}
.follow .info{align-items:center}
.follow .info span{font-size:12px;line-height:15px}
</style>
</head>
<body>
<div class="topbar">FREE SHIPPING &amp; FREE RETURNS</div>

<header class="header">
  <div class="brand">Lovmira<span class="dot"></span></div>
  <nav class="nav">
    <span class="active">HOME</span><span>PRODUCTS</span><span>NEWS</span><span>ABOUT US</span><span>CONTACT US</span>
    <span class="icon-btn" style="margin-left:0"><svg width="16" height="16" viewBox="0 0 16 16"><circle cx="7" cy="7" r="5" fill="none" stroke="#e10a14" stroke-width="2"/><line x1="11" y1="11" x2="15" y2="15" stroke="#e10a14" stroke-width="2"/></svg></span>
    <span class="icon-btn cart"><svg width="18" height="16" viewBox="0 0 18 16"><path d="M1 2h3l2 9h9l2-7H5" fill="none" stroke="#6b9b3a" stroke-width="2"/><circle cx="7" cy="14" r="1.5" fill="#6b9b3a"/><circle cx="14" cy="14" r="1.5" fill="#6b9b3a"/></svg></span>
  </nav>
</header>

<section class="hero" role="img" aria-label="Laser cut wedding invitation card on a kraft envelope on dark wood">
  <div class="hero-copy">
    <h1>Wedding Day</h1>
    <p>A very delicacy and connotation announcement</p>
    <span class="btn">SHOP NOW</span>
  </div>
  <div class="dots"><span></span><span class="on"></span><span></span></div>
</section>

<section class="categories">
  <h2 class="section-title">Our Categories</h2>
  <div class="grid" style="margin-top:40px">
    <div class="cat-card"><div class="media" role="img" aria-label="Pink laser cut invitation boxes" style="background:linear-gradient(160deg,#f3d6dc,#e7b8c2)"></div><div class="label">Laser Cut<br>Wedding Invitation</div></div>
    <div class="cat-card"><div class="media" role="img" aria-label="Popup wedding invitation card" style="background:linear-gradient(160deg,#f6e3e6,#e9c2c9)"></div><div class="label">Popup<br>Wedding Invitation</div></div>
    <div class="cat-card"><div class="media" role="img" aria-label="Vintage lace wedding invitation" style="background:linear-gradient(160deg,#efe8dc,#cdbfa7)"></div><div class="label">Vintage<br>Wedding Invitation</div></div>
    <div class="cat-card"><div class="media" role="img" aria-label="Handmade kraft wedding invitation" style="background:linear-gradient(160deg,#a07650,#6b4a30)"></div><div class="label">Handmade<br>Wedding Invitation</div></div>
  </div>
</section>

<section class="products featured">
  <h2 class="section-title">Featured Products</h2>
  <div class="grid" style="margin-top:32px">
    <div class="product"><div class="media" role="img" aria-label="Burgundy invitation with ribbon" style="background:linear-gradient(160deg,#8a4a5a,#5a2a34)"><span class="heart"><svg width="16" height="14" viewBox="0 0 16 14"><path d="M8 13L2 7a3.5 3.5 0 0 1 6-4 3.5 3.5 0 0 1 6 4z" fill="#fff"/></svg></span></div><div class="stars">★★★★★</div><h3>Product Name</h3><div class="model">Model No. : ICS0101</div><div class="price">$25.99</div></div>
    <div class="product"><div class="media" role="img" aria-label="Kraft invitation with lace" style="background:linear-gradient(160deg,#9b6c44,#6e4a2c)"><span class="heart"><svg width="16" height="14" viewBox="0 0 16 14"><path d="M8 13L2 7a3.5 3.5 0 0 1 6-4 3.5 3.5 0 0 1 6 4z" fill="#fff"/></svg></span><span class="add-cart">ADD TO CART</span></div><div class="stars">★★★★★</div><h3>Product Name</h3><div class="model">Model No. : ICS0101</div><div class="price">$25.99</div></div>
    <div class="product"><div class="media" role="img" aria-label="White laser cut invitation cards" style="background:linear-gradient(160deg,#f2efe9,#d8d2c6)"><span class="heart"><svg width="16" height="14" viewBox="0 0 16 14"><path d="M8 13L2 7a3.5 3.5 0 0 1 6-4 3.5 3.5 0 0 1 6 4z" fill="#fff"/></svg></span></div><div class="stars">★★★★★</div><h3>Product Name</h3><div class="model">Model No. : ICS0101</div><div class="price">$25.99</div></div>
    <div class="product"><div class="media" role="img" aria-label="Navy invitation with white lace" style="background:linear-gradient(160deg,#3d4f74,#c9a87c)"><span class="heart"><svg width="16" height="14" viewBox="0 0 16 14"><path d="M8 13L2 7a3.5 3.5 0 0 1 6-4 3.5 3.5 0 0 1 6 4z" fill="#fff"/></svg></span></div><div class="stars">★★★★★</div><h3>Product Name</h3><div class="model">Model No. : ICS0101</div><div class="price">$25.99</div></div>
  </div>
</section>

<section class="about">
  <div class="about-copy">
    <h2>About Us</h2>
    <p>We design and craft wedding invitations with care, from laser cut lace to popup scenes and handmade kraft cards. Every piece is cut, folded and checked by our own team, so each couple receives stationery that feels personal, elegant and ready for their day. We ship to Europe and the USA with friendly support.</p>
    <span class="btn">READ MORE</span>
  </div>
  <div class="about-media" role="img" aria-label="Green laser cut invitation with names beside pink flowers"></div>
</section>

<section class="products new">
  <h2 class="section-title">New Products</h2>
  <div class="grid" style="margin-top:32px">
    <div class="product"><div class="media" role="img" aria-label="Kraft laser cut invitation" style="background:linear-gradient(160deg,#b58a5e,#7a5434)"><span class="heart"><svg width="16" height="14" viewBox="0 0 16 14"><path d="M8 13L2 7a3.5 3.5 0 0 1 6-4 3.5 3.5 0 0 1 6 4z" fill="#fff"/></svg></span></div><div class="stars">★★★★★</div><h3>Product Name</h3><div class="model">Model No. : ICS0101</div><div class="price">$25.99</div></div>
    <div class="product"><div class="media" role="img" aria-label="Gold laser cut invitation on wood" style="background:linear-gradient(160deg,#8a5e3a,#c9a070)"><span class="heart"><svg width="16" height="14" viewBox="0 0 16 14"><path d="M8 13L2 7a3.5 3.5 0 0 1 6-4 3.5 3.5 0 0 1 6 4z" fill="#fff"/></svg></span></div><div class="stars">★★★★★</div><h3>Product Name</h3><div class="model">Model No. : ICS0101</div><div class="price">$25.99</div></div>
    <div class="product"><div class="media" role="img" aria-label="Pink popup invitation card" style="background:linear-gradient(160deg,#f1cfd6,#d98b9c)"><span class="heart"><svg width="16" height="14" viewBox="0 0 16 14"><path d="M8 13L2 7a3.5 3.5 0 0 1 6-4 3.5 3.5 0 0 1 6 4z" fill="#fff"/></svg></span></div><div class="stars">★★★★★</div><h3>Product Name</h3><div class="model">Model No. : ICS0101</div><div class="price">$25.99</div></div>
    <div class="product"><div class="media" role="img" aria-label="Vintage lace invitation" style="background:linear-gradient(160deg,#eee7da,#c6b79e)"><span class="heart"><svg width="16" height="14" viewBox="0 0 16 14"><path d="M8 13L2 7a3.5 3.5 0 0 1 6-4 3.5 3.5 0 0 1 6 4z" fill="#fff"/></svg></span></div><div class="stars">★★★★★</div><h3>Product Name</h3><div class="model">Model No. : ICS0101</div><div class="price">$25.99</div></div>
  </div>
</section>

<section class="promo">
  <div class="art" role="img" aria-label="White line illustration of two birds on a branch"></div>
  <div>
    <p>Sed ut perspiciatis unde omnis iste natus error sit volupta tem accusantium doloremque laudantium</p>
    <div class="shop">Vendoro</div>
  </div>
</section>

<footer class="footer">
  <div class="foot-brand">
    <div class="brand">Lovmira<span class="dot"></span></div>
    <small>© Copyrights 2022 All Rights Reserved.</small>
  </div>
  <div class="foot-col address">
    <h4>ADDRESS</h4>
    <div class="info"><span class="circle"><svg width="12" height="16" viewBox="0 0 12 16"><path d="M6 15s5-6 5-9A5 5 0 0 0 1 6c0 3 5 9 5 9z" fill="none" stroke="#fff" stroke-width="1.5"/><circle cx="6" cy="6" r="1.8" fill="#fff"/></svg></span><div><b>ADDRESS</b>Room 402, 4th Floor Harbor Building,<br>Lake Road, Fairview 510000</div></div>
    <div class="info"><span class="circle"><svg width="14" height="14" viewBox="0 0 14 14"><path d="M3 1l2 3-1.5 1.5a8 8 0 0 0 5 5L10 9l3 2-1 2C6 13 1 8 1 2z" fill="#fff"/></svg></span><div><b>PHONE</b>+1 555 012 3488</div></div>
    <div class="info"><span class="circle"><svg width="14" height="10" viewBox="0 0 14 10"><rect x="0.75" y="0.75" width="12.5" height="8.5" fill="none" stroke="#fff" stroke-width="1.5"/><path d="M1 1l6 5 6-5" fill="none" stroke="#fff" stroke-width="1.5"/></svg></span><div><b>EMAIL</b>admin@bluestonecraft.com</div></div>
  </div>
  <div class="foot-col links">
    <h4>LINKS</h4>
    <ul><li>Home</li><li>Products</li><li>News</li><li>About us</li><li>Contact Us</li></ul>
  </div>
  <div class="foot-col follow">
    <h4>FOLLOW US</h4>
    <div class="info"><span class="circle"></span><span>Like us on<br>Pagebook</span></div>
    <div class="info"><span class="circle"></span><span>Follow us on<br>Chirper</span></div>
    <div class="info"><span class="circle"></span><span>Follow us on<br>LinkPro</span></div>
  </div>
</footer>
</body>
</html>
```